Application Dashboard Skin - Non coded theme only

We are looking for a website color theme/look feel for a new .net dashboard application we are building. Target audience who will be using this are E and C level professionals. We are looking for the following:

Images of optional color themes for our existing dashboard. You can access a temporary version with no styling here: http://demo.plexaroni-app.com:99/ . Application built in telerik and highcharts.

We are not looking for finished code or application skins. Our development team will take your final design (with specific colors/images/etc. provided) and apply it to the final beta version of the application.

Design considerations:
We are open to creative ideas, but please know that preference will be given to professional designs with emphasis on a consistent brand look/feel. Designs and colors should be focused on quickly identifying and processing the data.

Multiple submissions welcome.

-Quorventa team

Target Market(s)

IT / Insurance

Industry/Entity Type

Building

Number of Pages Required

3 page

Requirements
Must have
• Application Dashboard link for design: http://demo.plexaroni-app.com:99/

```html
<!DOCTYPE html>
<html lang="en">
<head>
<meta charset="utf-8">
<title>Ledgerview – Accuracy Results</title>
<link href="https://fonts.googleapis.com/css2?family=Lato:wght@400;700&display=swap" rel="stylesheet">
<style>
:root{
  --sidebar:#2e313a;
  --sidebar-text:#d9dce2;
  --page:#eceef1;
  --panel:#ffffff;
  --panel-head:#f7f8f9;
  --line:#dfe2e6;
  --text:#3a3d44;
  --muted:#8b9098;
  --teal:#2fb8c3;
  --dark:#3a3d44;
  --bar:#d8dbdf;
}
*{box-sizing:border-box;margin:0;padding:0}
html,body{width:791px;height:1200px;overflow:hidden}
body{font-family:"Lato",sans-serif;color:var(--text);background:var(--page);display:flex}
.sidebar{width:132px;height:1200px;background:var(--sidebar);color:var(--sidebar-text);position:relative;flex:none}
.brand{padding:16px 18px 22px}
.brand-name{font-size:15px;font-weight:400;color:#fff;letter-spacing:.3px}
.nav{list-style:none}
.nav li{font-size:10px;padding:7px 18px}
.nav li.active{color:#fff;font-weight:700}
.copyright{position:absolute;bottom:12px;left:10px;font-size:6px;color:#8a8e97;white-space:nowrap}
.main{flex:1;padding:12px;display:flex;flex-direction:column;gap:12px}
.panel{background:var(--panel);border:1px solid var(--line)}
.panel-head{display:flex;justify-content:space-between;align-items:center;height:28px;padding:0 10px;background:var(--panel-head);border-bottom:1px solid var(--line)}
.panel-title{font-size:9px;font-weight:700;letter-spacing:.4px;text-transform:uppercase}
.select{font-size:7px;color:var(--muted);border:1px solid var(--line);background:#fff;padding:3px 8px;border-radius:2px}
.panel-body{padding:10px}
.card{border:1px solid var(--line);background:#fff;padding:8px}
.card-title{text-align:center;font-size:10px;font-weight:700}
.card-sub{text-align:center;font-size:7px;color:var(--muted);margin-top:2px}
.credit{text-align:right;font-size:6px;color:#b4b8be}
.tabs{display:flex;border-bottom:1px solid var(--line);margin-bottom:10px}
.tab{font-size:7px;padding:6px 10px;color:var(--muted)}
.tab.active{color:var(--text);border:1px solid var(--line);border-bottom-color:#fff;margin-bottom:-1px;background:#fff}
.split{display:flex;gap:10px}
.split>.card{flex:1}
.kpi-list{list-style:none;margin-top:8px}
.kpi-list li{display:flex;align-items:center;font-size:7px;height:21px;border-bottom:1px solid #f0f1f3}
.kpi-icon{width:9px;height:9px;border-radius:50%;background:var(--teal);margin-right:7px;flex:none}
.kpi-label{flex:1}
.kpi-value{width:70px;color:var(--muted)}
.pie-stack{flex:1;display:flex;flex-direction:column;gap:10px}
.pie-stack .card{flex:1}
svg text{font-family:"Lato",sans-serif}
</style>
</head>
<body>
<aside class="sidebar">
  <div class="brand"><span class="brand-name">Ledgerview</span></div>
  <ul class="nav">
    <li class="active">Accuracy Results</li>
    <li>Processor Accuracy</li>
    <li>Manage Users</li>
    <li>Settings</li>
  </ul>
  <p class="copyright">© 2016 Ledgerview. All Rights Reserved.</p>
</aside>

<main class="main">
  <section class="panel accuracy" style="height:356px">
    <header class="panel-head"><h2 class="panel-title">Accuracy Results</h2><span class="select">Select Year ▾</span></header>
    <div class="panel-body">
      <div class="card" style="height:305px">
        <p class="card-title">YTD Overall Accuracy</p>
        <p class="card-sub">Click the bars to view YTD details for the specific region</p>
        <svg width="595" height="260" viewBox="0 0 595 260">
          <g stroke="#eef0f2"><line x1="50" y1="30" x2="580" y2="30"/><line x1="50" y1="80" x2="580" y2="80"/><line x1="50" y1="130" x2="580" y2="130"/><line x1="50" y1="180" x2="580" y2="180"/></g>
          <line x1="50" y1="225" x2="580" y2="225" stroke="#c9cdd2"/>
          <g font-size="7" fill="#8b9098" text-anchor="end"><text x="44" y="33">100%</text><text x="44" y="83">75%</text><text x="44" y="133">50%</text><text x="44" y="183">25%</text><text x="44" y="228">0%</text></g>
          <text x="14" y="130" font-size="7" fill="#8b9098" transform="rotate(-90 14 130)" text-anchor="middle">Accuracy</text>
          <g fill="var(--bar)">
            <rect x="78" y="39" width="56" height="186"/>
            <rect x="183" y="40" width="56" height="185"/>
            <rect x="288" y="42" width="56" height="183"/>
            <rect x="393" y="45" width="56" height="180"/>
            <rect x="498" y="84" width="56" height="141"/>
          </g>
          <g font-size="7" font-weight="700" fill="#3a3d44" text-anchor="middle">
            <text x="106" y="34">95.5%</text><text x="211" y="35">95.1%</text><text x="316" y="37">94.6%</text><text x="421" y="40">94.0%</text><text x="526" y="79">73.5%</text>
          </g>
          <g font-size="7" fill="#5b6068" text-anchor="middle">
            <text x="106" y="238">Colorado</text><text x="211" y="238">Georgia</text><text x="316" y="238">Hawaii</text><text x="421" y="238">Middletown</text><text x="526" y="238">Northfield</text>
          </g>
        </svg>
        <p class="credit">chart source</p>
      </div>
    </div>
  </section>

  <section class="panel errors" style="height:372px">
    <header class="panel-head"><h2 class="panel-title">Error Impact for June 2016</h2><span class="select">All Regions ▾</span></header>
    <div class="panel-body">
      <nav class="tabs"><span class="tab active">All Errors</span><span class="tab">Providers</span><span class="tab">Employees</span><span class="tab">Line Of Business</span></nav>
      <div class="split">
        <div class="card" style="height:285px">
          <p class="card-title">Top 10 Error Reasons</p>
          <p class="card-sub">All Regions</p>
          <svg width="290" height="240" viewBox="0 0 290 240">
            <g font-size="6" fill="#5b6068" text-anchor="end">
              <text x="74" y="18">Incorrect Coding</text><text x="74" y="38">Claim Held Incorr.</text><text x="74" y="58">Bill to Wrong Member</text><text x="74" y="78">Incorrect Pricing</text><text x="74" y="98">Copay Amount Err.</text><text x="74" y="118">Did Not Follow Proc.</text><text x="74" y="138">Did Not Follow Proc.</text><text x="74" y="158">Claim Denied in Err.</text><text x="74" y="178">Calculation Error</text><text x="74" y="198">Duplicate Payment</text>
            </g>
            <line x1="80" y1="6" x2="80" y2="205" stroke="#c9cdd2"/>
            <g fill="var(--bar)">
              <rect x="80" y="12" width="150" height="9"/><rect x="80" y="32" width="118" height="9"/><rect x="80" y="52" width="92" height="9"/><rect x="80" y="72" width="74" height="9"/><rect x="80" y="92" width="66" height="9"/><rect x="80" y="112" width="56" height="9"/><rect x="80" y="132" width="48" height="9"/><rect x="80" y="152" width="40" height="9"/><rect x="80" y="172" width="34" height="9"/><rect x="80" y="192" width="30" height="9"/>
            </g>
            <g font-size="6" fill="#3a3d44"><text x="234" y="19">86</text><text x="202" y="39">68</text><text x="176" y="59">53</text><text x="158" y="79">42</text><text x="150" y="99">38</text><text x="140" y="119">32</text><text x="132" y="139">28</text><text x="124" y="159">23</text><text x="118" y="179">20</text><text x="114" y="199">17</text></g>
            <line x1="80" y1="205" x2="280" y2="205" stroke="#c9cdd2"/>
            <text x="180" y="222" font-size="6" fill="#8b9098" text-anchor="middle">Errors</text>
          </svg>
        </div>
        <div class="card" style="height:285px">
          <p class="card-title">Top 10 Error Reasons - Financial Impact</p>
          <p class="card-sub">All Regions</p>
          <svg width="290" height="240" viewBox="0 0 290 240">
            <g font-size="6" fill="#5b6068" text-anchor="end">
              <text x="74" y="18">Incorrect Coding</text><text x="74" y="38">Claim Held Incorr.</text><text x="74" y="58">Bill to Wrong Member</text><text x="74" y="78">Incorrect Pricing</text><text x="74" y="98">Copay Amount Err.</text><text x="74" y="118">Did Not Follow Proc.</text><text x="74" y="138">Did Not Follow Proc.</text><text x="74" y="158">Claim Denied in Err.</text><text x="74" y="178">Calculation Error</text><text x="74" y="198">Duplicate Payment</text>
            </g>
            <line x1="80" y1="6" x2="80" y2="205" stroke="#c9cdd2"/>
            <g fill="var(--bar)">
              <rect x="80" y="12" width="130" height="9"/><rect x="80" y="92" width="40" height="9"/><rect x="80" y="112" width="30" height="9"/><rect x="80" y="132" width="24" height="9"/><rect x="80" y="152" width="18" height="9"/><rect x="80" y="172" width="14" height="9"/><rect x="80" y="192" width="10" height="9"/>
            </g>
            <g fill="var(--teal)"><rect x="80" y="32" width="48" height="9"/><rect x="80" y="52" width="72" height="9"/><rect x="80" y="72" width="110" height="9"/></g>
            <g font-size="6" fill="#3a3d44"><text x="214" y="19">$ 18,210.44</text><text x="132" y="39">$ -3,406.11</text><text x="156" y="59">$ -5,120.92</text><text x="194" y="79">$ -7,904.20</text><text x="124" y="99">$ 2,861.50</text><text x="114" y="119">$ 2,104.18</text><text x="108" y="139">$ 1,712.33</text><text x="102" y="159">$ 1,250.07</text><text x="98" y="179">$ 980.45</text><text x="94" y="199">$ 702.16</text></g>
            <line x1="80" y1="205" x2="280" y2="205" stroke="#c9cdd2"/>
            <text x="180" y="222" font-size="6" fill="#8b9098" text-anchor="middle">$ Amount</text>
          </svg>
        </div>
      </div>
    </div>
  </section>

  <section class="panel kpis" style="height:400px">
    <header class="panel-head"><h2 class="panel-title">KPI's</h2><span class="select">All Regions ▾</span></header>
    <div class="panel-body split">
      <div class="card" style="height:355px">
        <p class="card-title">Overall YTD Accuracy</p>
        <p class="card-sub">94.6%</p>
        <ul class="kpi-list">
          <li><span class="kpi-icon"></span><span class="kpi-label">Claims Audited</span><span class="kpi-value">1,893</span></li>
          <li><span class="kpi-icon"></span><span class="kpi-label">Avg. Claims Audited per day</span><span class="kpi-value">18</span></li>
          <li><span class="kpi-icon"></span><span class="kpi-label">Errors Found</span><span class="kpi-value">104</span></li>
          <li><span class="kpi-icon"></span><span class="kpi-label">Financial Impact</span><span class="kpi-value">$ 24,681.07</span></li>
          <li><span class="kpi-icon"></span><span class="kpi-label">Total Claims Posted</span><span class="kpi-value">1,172,524</span></li>
          <li><span class="kpi-icon"></span><span class="kpi-label">Total Encounter Claims</span><span class="kpi-value">84,806</span></li>
          <li><span class="kpi-icon"></span><span class="kpi-label">Total Non-Adjudication Claim Count</span><span class="kpi-value">48,218</span></li>
          <li><span class="kpi-icon"></span><span class="kpi-label">Total Adjustment Claim Count</span><span class="kpi-value">36,592</span></li>
          <li><span class="kpi-icon"></span><span class="kpi-label">Total Denied Claim Count</span><span class="kpi-value">92,146</span></li>
          <li><span class="kpi-icon"></span><span class="kpi-label">Total Dollars Paid</span><span class="kpi-value">$ 88,410,372</span></li>
          <li><span class="kpi-icon"></span><span class="kpi-label">Auto Adjudication Rate</span><span class="kpi-value">62.4%</span></li>
          <li><span class="kpi-icon"></span><span class="kpi-label">Adjustment Rate</span><span class="kpi-value">3.1%</span></li>
          <li><span class="kpi-icon"></span><span class="kpi-label">Denial Rate</span><span class="kpi-value">7.9%</span></li>
        </ul>
      </div>
      <div class="pie-stack">
        <div class="card">
          <p class="card-title">Paid vs. Denied</p>
          <svg width="290" height="140" viewBox="0 0 290 140">
            <circle cx="150" cy="72" r="58" fill="var(--teal)"/>
            <path d="M150 72 L150 14 A58 58 0 0 1 180 22 Z" fill="var(--dark)"/>
            <g font-size="6" fill="#5b6068"><text x="190" y="14">Denied: 8.0%</text><text x="48" y="82">Paid: 92.0%</text></g>
            <g stroke="#9ca1a8" stroke-width=".6"><line x1="168" y1="16" x2="188" y2="12"/><line x1="92" y1="78" x2="80" y2="80"/></g>
          </svg>
        </div>
        <div class="card">
          <p class="card-title">Paid vs. Encounter</p>
          <svg width="290" height="140" viewBox="0 0 290 140">
            <circle cx="150" cy="72" r="58" fill="var(--teal)"/>
            <path d="M150 72 L150 14 A58 58 0 0 0 108 32 Z" fill="var(--dark)"/>
            <g font-size="6" fill="#5b6068"><text x="66" y="16">Encounter: 7.2%</text><text x="52" y="124">Paid: 92.8%</text></g>
            <g stroke="#9ca1a8" stroke-width=".6"><line x1="128" y1="18" x2="112" y2="14"/><line x1="120" y1="118" x2="88" y2="122"/></g>
          </svg>
        </div>
      </div>
    </div>
  </section>
</main>
</body>
</html>
```